Healthcare Seminar Flyer

We will be holding a Healthcare (HIPAA) and Cybersecurity seminar, and would like a flyer to hand out to potential participants.

Target Market(s)

Healthcare

Colors
0054AA
0677BA
7BADD7
CADEEF
E8F1F8

Requirements
Must have
• See attached word document

```html
<!DOCTYPE html>
<html lang="en">
<head>
<meta charset="utf-8">
<title>HIPAA Compliance Officer Course Flyer</title>
<link href="https://fonts.googleapis.com/css2?family=Poppins:ital,wght@0,500;0,600;0,700;1,500&family=Roboto:ital,wght@0,400;0,500;0,700;1,400;1,500&display=swap" rel="stylesheet">
<style>
:root{
  --stage:#dcdadb;
  --ink:#111827;
  --navy:#0f2b5c;
  --white:#ffffff;
  --top:#efeff3;
}
.theme-blue{
  --accent:#0054AA;
  --circle:#7BADD7;
  --panel:#E3EBF4;
  --band:#0A4FA0;
  --title-accent:#0054AA;
}
.theme-sand{
  --accent:#3AB0DC;
  --circle:#3AB0DC;
  --panel:#F6E2C3;
  --band:#0D2A57;
  --title-accent:#3AB0DC;
}
*{margin:0;padding:0;box-sizing:border-box}
html,body{width:1200px;height:954px;overflow:hidden;background:var(--stage)}
.stage{position:relative;width:1200px;height:954px}
.flyer{position:absolute;top:172px;width:764px;height:988px;transform:scale(.6);transform-origin:0 0;
  background:var(--panel);overflow:hidden;font-family:'Roboto',sans-serif;color:var(--ink);
  box-shadow:0 30px 50px rgba(0,0,0,.18)}
.flyer.left{left:130px}
.flyer.right{left:613px}
.top-band{position:absolute;left:0;top:0;width:100%;height:283px;background:var(--top)}
.title{position:absolute;left:48px;top:40px;font-family:'Poppins',sans-serif;font-weight:600;font-size:32px;line-height:39px;color:var(--ink);letter-spacing:.2px}
.title .hl{color:var(--title-accent)}
.event{position:absolute;right:26px;top:40px;text-align:right}
.event .date{font-family:'Poppins',sans-serif;font-weight:600;font-size:19.5px;color:var(--navy)}
.event .lunch{font-family:'Poppins',sans-serif;font-style:italic;font-weight:500;font-size:16.5px;color:var(--accent);margin-right:5px}
.event .venue{font-size:13.5px;line-height:16.5px;margin-top:21px;text-align:left;margin-left:auto;width:280px}
.art{position:absolute;left:36px;top:181px;width:282px;height:207px}
.price{position:absolute;right:26px;top:214px;text-align:right;font-family:'Poppins',sans-serif;font-weight:600;font-size:21.5px;line-height:26px}
.register{position:absolute;right:28px;top:298px;text-align:right}
.register .lbl{font-family:'Poppins',sans-serif;font-weight:700;font-size:21.5px;color:var(--accent)}
.register .url{font-size:22.5px;color:var(--navy);margin-top:2px}
.session{position:absolute;left:0;width:100%}
.presenter{position:absolute;left:32px;top:0;width:200px}
.presenter .topic{font-family:'Poppins',sans-serif;font-weight:500;font-size:15.5px;padding:2px 8px;
  background:linear-gradient(90deg,rgba(255,255,255,.75),rgba(255,255,255,0));width:190px}
.presenter .by{font-size:10px;letter-spacing:1px;margin:4px 0 0 8px}
.presenter .name{font-family:'Poppins',sans-serif;font-weight:600;font-size:13.5px;letter-spacing:.6px;margin-left:8px;line-height:15px}
.presenter .org{display:flex;align-items:center;gap:6px;margin:10px 0 0 8px;font-size:11px;font-weight:700;letter-spacing:.5px;color:var(--navy)}
.presenter .org i{display:block;width:9px;height:9px;background:var(--navy)}
.bullets{position:absolute;top:0;width:232px;list-style:none;font-size:10.8px;line-height:13.5px}
.bullets li{position:relative;padding-left:14px;margin-bottom:6.5px}
.bullets li::before{content:"";position:absolute;left:0;top:5px;width:4px;height:4px;border-radius:50%;background:var(--ink)}
.bullets.c1{left:240px}
.bullets.c2{left:501px}
.kit{position:absolute;left:0;top:781px;width:100%;height:207px;background:var(--band);color:var(--white);text-align:center}
.kit h2{font-family:'Roboto',sans-serif;font-weight:500;font-size:25px;margin-top:24px}
.kit .sub{font-style:italic;font-weight:500;font-size:14px;margin-top:6px}
.badge{position:absolute;left:641px;top:748px;width:78px;height:78px;border-radius:50%;background:var(--white);
  display:flex;align-items:center;justify-content:center;text-align:center;font-style:italic;font-weight:500;font-size:10.5px;line-height:13px;color:var(--navy)}
.features{position:absolute;left:0;top:90px;width:100%}
.feature{position:absolute;width:170px;text-align:center;font-style:italic;font-weight:500;font-size:10.8px;line-height:13.5px}
.feature svg{display:block;margin:0 auto 14px;width:34px;height:34px}
</style>
</head>
<body>
<div class="stage">

<!-- Blue flyer -->
<article class="flyer left theme-blue">
  <div class="top-band"></div>
  <h1 class="title"><span class="hl">HIPAA</span> COMPLIANCE<br>OFFICER COURSE WITH<br>CERTIFICATE</h1>
  <div class="event">
    <div class="date">August 25th, 9:30am to 3pm</div>
    <div class="lunch">(Lunch Included!)</div>
    <div class="venue">Grand Palm Hotel At Riverside Commons<br>4820 Riverside Commons Blvd Fort Myers, Fl 33912</div>
  </div>
  <svg class="art" viewBox="0 0 282 207">
    <circle cx="103" cy="103.5" r="103" fill="var(--circle)"/>
    <defs><radialGradient id="photoA" cx="45%" cy="55%" r="65%"><stop offset="0" stop-color="#b08a6e"/><stop offset=".55" stop-color="#5c5a62"/><stop offset="1" stop-color="#c9c3bd"/></radialGradient></defs>
    <circle cx="178" cy="103.5" r="103" fill="url(#photoA)" role="img" aria-label="Photo of professionals taking notes at a meeting table"/>
  </svg>
  <div class="price">Normally $299,<br>register now for only $49!</div>
  <div class="register"><div class="lbl">Register now at:</div><div class="url">http://regnow.link/hc24s</div></div>

  <section class="session" style="top:418px">
    <div class="presenter"><div class="topic">HIPAA Topics</div><div class="by">PRESENTED BY</div><div class="name">DANIEL HARTLEY,</div>
      <div class="org"><i></i>Keystone Compliance Group</div></div>
    <ul class="bullets c1"><li>Patient Access Guidance</li><li>What you can charge for medical records.</li><li>What is an Information Blocking?</li><li>How to respond legally to subpoenas.</li><li>The dangers of social media.</li></ul>
    <ul class="bullets c2"><li>Why do I have to have my business associate agreement updated?</li><li>Why your current policies could cause a penalty for Medicare Fraud.</li><li>What you should know about current OCR enforcement actions. (Actual cases and enforcement letters.)</li></ul>
  </section>
  <section class="session" style="top:546px">
    <div class="presenter"><div class="topic">Cyber-Security Review</div><div class="by">PRESENTED BY</div><div class="name">OWEN PIERCE</div>
      <div class="org"><i></i>Vantage IT Solutions</div></div>
    <ul class="bullets c1"><li>“How to avoid the $99 million dollar class action lawsuit”</li><li>Lessons from recent cybersecurity incidents (Actual cases)</li><li>New US Treasury Department sanctions and fines</li></ul>
    <ul class="bullets c2"><li>Questions that you MUST ask your IT provider</li><li>What to expect WHEN (not if) you have a cybersecurity event</li></ul>
  </section>
  <section class="session" style="top:673px">
    <div class="presenter"><div class="topic">Cyber Insurance</div><div class="by">PRESENTED BY</div><div class="name">LUCAS BENNETT</div>
      <div class="org"><i></i>Harbor Coast Insurers</div></div>
    <ul class="bullets c1"><li>The changing landscape of Cyber Insurance</li><li>“I had a breach, when should I contact my insurance agent?”</li></ul>
    <ul class="bullets c2"><li>What does Cyber Liability cover?</li></ul>
  </section>

  <div class="kit">
    <h2>Includes a FREE Information Blocking Kit!</h2>
    <div class="sub">Full Compliance Kit for Information Blocking that includes:</div>
    <div class="features">
      <div class="feature" style="left:28px"><svg viewBox="0 0 34 34" fill="none" stroke="#fff" stroke-width="2.2" stroke-linecap="round" stroke-linejoin="round"><path d="M16 5H8a4 4 0 0 0-4 4v17a4 4 0 0 0 4 4h17a4 4 0 0 0 4-4v-8"/><path d="M25 4l5 5-12 12h-5v-5z"/></svg>Updated for Information Blocking Business Associate Agreement.</div>
      <div class="feature" style="left:205px"><svg viewBox="0 0 34 34" fill="none" stroke="#fff" stroke-width="2.2" stroke-linecap="round"><circle cx="13" cy="11" r="6"/><path d="M3 29c0-6 4-10 10-10s10 4 10 10z"/><path d="M21 5a6 6 0 0 1 0 12M25 20c4 1 6 4 6 9"/></svg>Training on how to implement Information Blocking in your practice.</div>
      <div class="feature" style="left:385px"><svg viewBox="0 0 34 34" fill="none" stroke="#fff" stroke-width="2.2" stroke-linecap="round" stroke-linejoin="round"><rect x="4" y="4" width="26" height="26" rx="5"/><path d="M11 17l4 4 8-8"/></svg>Getting Started Guide and FACT Sheet.</div>
      <div class="feature" style="left:555px"><svg viewBox="0 0 34 34" fill="none" stroke="#fff" stroke-width="2.2" stroke-linecap="round"><path d="M3 17s5-9 14-9 14 9 14 9-5 9-14 9S3 17 3 17z"/><circle cx="17" cy="17" r="4.5"/><path d="M5 30L29 4"/></svg>Forms to document exceptions and other Information Blocking requirements.</div>
    </div>
  </div>
  <div class="badge">Hard Copy &amp;<br>Digital Copy</div>
</article>

<!-- Sand flyer -->
<article class="flyer right theme-sand">
  <div class="top-band"></div>
  <h1 class="title"><span class="hl">HIPAA</span> COMPLIANCE<br>OFFICER COURSE WITH<br>CERTIFICATE</h1>
  <div class="event">
    <div class="date">August 25th, 9:30am to 3pm</div>
    <div class="lunch">(Lunch Included!)</div>
    <div class="venue">Grand Palm Hotel At Riverside Commons<br>4820 Riverside Commons Blvd Fort Myers, Fl 33912</div>
  </div>
  <svg class="art" viewBox="0 0 282 207">
    <circle cx="103" cy="103.5" r="103" fill="var(--circle)"/>
    <defs><radialGradient id="photoB" cx="45%" cy="55%" r="65%"><stop offset="0" stop-color="#b08a6e"/><stop offset=".55" stop-color="#5c5a62"/><stop offset="1" stop-color="#c9c3bd"/></radialGradient></defs>
    <circle cx="178" cy="103.5" r="103" fill="url(#photoB)" role="img" aria-label="Photo of professionals taking notes at a meeting table"/>
  </svg>
  <div class="price">Normally $299,<br>register now for only $49!</div>
  <div class="register"><div class="lbl">Register now at:</div><div class="url">http://regnow.link/hc24s</div></div>

  <section class="session" style="top:418px">
    <div class="presenter"><div class="topic">HIPAA Topics</div><div class="by">PRESENTED BY</div><div class="name">DANIEL HARTLEY,</div>
      <div class="org"><i></i>Keystone Compliance Group</div></div>
    <ul class="bullets c1"><li>Patient Access Guidance</li><li>What you can charge for medical records.</li><li>What is an Information Blocking?</li><li>How to respond legally to subpoenas.</li><li>The dangers of social media.</li></ul>
    <ul class="bullets c2"><li>Why do I have to have my business associate agreement updated?</li><li>Why your current policies could cause a penalty for Medicare Fraud.</li><li>What you should know about current OCR enforcement actions. (Actual cases and enforcement letters.)</li></ul>
  </section>
  <section class="session" style="top:546px">
    <div class="presenter"><div class="topic">Cyber-Security Review</div><div class="by">PRESENTED BY</div><div class="name">OWEN PIERCE</div>
      <div class="org"><i></i>Vantage IT Solutions</div></div>
    <ul class="bullets c1"><li>“How to avoid the $99 million dollar class action lawsuit”</li><li>Lessons from recent cybersecurity incidents (Actual cases)</li><li>New US Treasury Department sanctions and fines</li></ul>
    <ul class="bullets c2"><li>Questions that you MUST ask your IT provider</li><li>What to expect WHEN (not if) you have a cybersecurity event</li></ul>
  </section>
  <section class="session" style="top:673px">
    <div class="presenter"><div class="topic">Cyber Insurance</div><div class="by">PRESENTED BY</div><div class="name">LUCAS BENNETT</div>
      <div class="org"><i></i>Harbor Coast Insurers</div></div>
    <ul class="bullets c1"><li>The changing landscape of Cyber Insurance</li><li>“I had a breach, when should I contact my insurance agent?”</li></ul>
    <ul class="bullets c2"><li>What does Cyber Liability cover?</li></ul>
  </section>

  <div class="kit">
    <h2>Includes a FREE Information Blocking Kit!</h2>
    <div class="sub">Full Compliance Kit for Information Blocking that includes:</div>
    <div class="features">
      <div class="feature" style="left:28px"><svg viewBox="0 0 34 34" fill="none" stroke="#fff" stroke-width="2.2" stroke-linecap="round" stroke-linejoin="round"><path d="M16 5H8a4 4 0 0 0-4 4v17a4 4 0 0 0 4 4h17a4 4 0 0 0 4-4v-8"/><path d="M25 4l5 5-12 12h-5v-5z"/></svg>Updated for Information Blocking Business Associate Agreement.</div>
      <div class="feature" style="left:205px"><svg viewBox="0 0 34 34" fill="none" stroke="#fff" stroke-width="2.2" stroke-linecap="round"><circle cx="13" cy="11" r="6"/><path d="M3 29c0-6 4-10 10-10s10 4 10 10z"/><path d="M21 5a6 6 0 0 1 0 12M25 20c4 1 6 4 6 9"/></svg>Training on how to implement Information Blocking in your practice.</div>
      <div class="feature" style="left:385px"><svg viewBox="0 0 34 34" fill="none" stroke="#fff" stroke-width="2.2" stroke-linecap="round" stroke-linejoin="round"><rect x="4" y="4" width="26" height="26" rx="5"/><path d="M11 17l4 4 8-8"/></svg>Getting Started Guide and FACT Sheet.</div>
      <div class="feature" style="left:555px"><svg viewBox="0 0 34 34" fill="none" stroke="#fff" stroke-width="2.2" stroke-linecap="round"><path d="M3 17s5-9 14-9 14 9 14 9-5 9-14 9S3 17 3 17z"/><circle cx="17" cy="17" r="4.5"/><path d="M5 30L29 4"/></svg>Forms to document exceptions and other Information Blocking requirements.</div>
    </div>
  </div>
  <div class="badge">Hard Copy &amp;<br>Digital Copy</div>
</article>

</div>
</body>
</html>
```